Stationery Project with Logo Design

We need stationery & logo design for a new small boutique marketing company based in Perth Western Australia. The company is called Blue Harbor Marketing.

We offer marketing services to small-to-medium business.

We would like to see designs strong & innovative designs and should use red as one of the colours.

The final design should communicate innovation and fun.

Target Market(s)

Small to medium business owners between 20 - 50 years

Industry/Entity Type

Business

Logo Text

```html
<!DOCTYPE html>
<html lang="en">
<head>
<meta charset="utf-8">
<title>Blue Harbor Marketing – Business Cards</title>
<link rel="stylesheet" href="https://fonts.googleapis.com/css2?family=Montserrat:wght@300;400;600&display=swap">
<style>
  :root {
    --backdrop: #3b3b3d;
    --card-light: #eeede8;
    --card-dark: #2a2b2e;
    --brand-red: #c8202a;
    --ink-dark: #55565a;
    --ink-light: #e6e6e6;
    --ink-muted: #b9babd;
  }
  * { margin: 0; padding: 0; box-sizing: border-box; }
  html, body { width: 1200px; height: 900px; overflow: hidden; }
  body {
    background: var(--backdrop);
    font-family: "Montserrat", Arial, sans-serif;
    display: flex;
    flex-direction: column;
    align-items: center;
    justify-content: center;
    gap: 34px;
  }
  .card {
    position: relative;
    width: 700px;
    height: 400px;
    border-radius: 3px;
  }
  .card--light { background: var(--card-light); color: var(--ink-dark); }
  .card--dark { background: var(--card-dark); color: var(--ink-light); }

  .wordmark {
    position: absolute;
    left: 0; right: 0;
    top: 92px;
    text-align: center;
    color: var(--brand-red);
    font-weight: 300;
    line-height: 1;
  }
  .wordmark__name { font-size: 58px; letter-spacing: 1px; }
  .wordmark__line { font-size: 19px; letter-spacing: 9px; margin-top: 8px; padding-left: 190px; }

  .contacts {
    position: absolute;
    top: 242px;
    left: 236px;
    display: grid;
    grid-template-columns: 200px 220px;
    row-gap: 10px;
    font-size: 13px;
    font-weight: 300;
  }
  .contact { display: flex; align-items: center; gap: 8px; }
  .contact__icon { width: 16px; height: 16px; flex: none; }

  .person {
    position: absolute;
    left: 44px;
    bottom: 40px;
  }
  .person__name { font-size: 19px; font-weight: 600; letter-spacing: 0.5px; }
  .person__role { font-size: 14px; font-weight: 300; margin-top: 3px; }
  .card--dark .person__role { color: var(--ink-muted); }
</style>
</head>
<body>

  <section class="card card--light">
    <div class="wordmark">
      <div class="wordmark__name">BLUE HARBOR</div>
      <div class="wordmark__line">MARKETING</div>
    </div>
    <div class="contacts">
      <div class="contact">
        <svg class="contact__icon" viewBox="0 0 16 16"><circle cx="8" cy="8" r="8" fill="#c8202a"/><path d="M5.2 4.2l1.4-.2.8 2-1 .8a5 5 0 0 0 2.8 2.8l.8-1 2 .8-.2 1.4c-3.8.4-7-2.8-6.6-6.6z" fill="#fff"/></svg>
        <span>(555) 014-2087</span>
      </div>
      <div class="contact">
        <svg class="contact__icon" viewBox="0 0 16 16"><circle cx="8" cy="8" r="8" fill="#c8202a"/><rect x="4" y="5.2" width="8" height="5.6" fill="none" stroke="#fff" stroke-width="1"/><path d="M4 5.4l4 3 4-3" fill="none" stroke="#fff" stroke-width="1"/></svg>
        <span>dana@blueharbor.com</span>
      </div>
      <div class="contact">
        <svg class="contact__icon" viewBox="0 0 16 16"><circle cx="8" cy="8" r="8" fill="#c8202a"/></svg>
        <span>blueharbor</span>
      </div>
      <div class="contact">
        <svg class="contact__icon" viewBox="0 0 16 16"><circle cx="8" cy="8" r="8" fill="#c8202a"/><circle cx="8" cy="8" r="4" fill="none" stroke="#fff" stroke-width="1"/><path d="M4 8h8M8 4c-2 2.4-2 5.6 0 8M8 4c2 2.4 2 5.6 0 8" fill="none" stroke="#fff" stroke-width="0.8"/></svg>
        <span>www.blueharbor.com</span>
      </div>
    </div>
    <div class="person">
      <div class="person__name">DANA MORROW</div>
      <div class="person__role">Founder &amp; CEO</div>
    </div>
  </section>

  <section class="card card--dark">
    <div class="wordmark">
      <div class="wordmark__name">BLUE HARBOR</div>
      <div class="wordmark__line">MARKETING</div>
    </div>
    <div class="contacts">
      <div class="contact">
        <svg class="contact__icon" viewBox="0 0 16 16"><circle cx="8" cy="8" r="8" fill="#c8202a"/><path d="M5.2 4.2l1.4-.2.8 2-1 .8a5 5 0 0 0 2.8 2.8l.8-1 2 .8-.2 1.4c-3.8.4-7-2.8-6.6-6.6z" fill="#fff"/></svg>
        <span>(555) 014-2087</span>
      </div>
      <div class="contact">
        <svg class="contact__icon" viewBox="0 0 16 16"><circle cx="8" cy="8" r="8" fill="#c8202a"/><rect x="4" y="5.2" width="8" height="5.6" fill="none" stroke="#fff" stroke-width="1"/><path d="M4 5.4l4 3 4-3" fill="none" stroke="#fff" stroke-width="1"/></svg>
        <span>dana@blueharbor.com</span>
      </div>
      <div class="contact">
        <svg class="contact__icon" viewBox="0 0 16 16"><circle cx="8" cy="8" r="8" fill="#c8202a"/></svg>
        <span>blueharbor</span>
      </div>
      <div class="contact">
        <svg class="contact__icon" viewBox="0 0 16 16"><circle cx="8" cy="8" r="8" fill="#c8202a"/><circle cx="8" cy="8" r="4" fill="none" stroke="#fff" stroke-width="1"/><path d="M4 8h8M8 4c-2 2.4-2 5.6 0 8M8 4c2 2.4 2 5.6 0 8" fill="none" stroke="#fff" stroke-width="0.8"/></svg>
        <span>www.blueharbor.com</span>
      </div>
    </div>
    <div class="person">
      <div class="person__name">DANA MORROW</div>
      <div class="person__role">Founder &amp; CEO</div>
    </div>
  </section>

</body>
</html>
```